KVO-Business Card Design

I need a modern, professional business card design that includes my logo as the main feature, maybe the entire background with the contact info overlaying or even contact info on the back and the logo full frontal

Neat and organized placement of contact information

Would like to see options in black and white

Target Market(s)

real estate Developers, Construction managers, business and home owners

Industry/Entity Type

Construction

Contact Information for Business Card

KVO Construction
Danny Ferrante
General Contractor

Office: 1-888-902-7315 Ext #1
Cell: 215-730-4162
Fax: 1-888-902-7315

Font styles to use
Serif

Requirements
Must have
• title
• office #
• cell #
• Email
• website
Nice to have
• fax

```html
<!DOCTYPE html>
<html lang="en">
<head>
<meta charset="utf-8">
<title>KVO-Business Card Design</title>
<link rel="stylesheet" href="https://fonts.googleapis.com/css2?family=Roboto+Slab:wght@400;700&display=swap">
<style>
  :root {
    --canvas: #ecebe8;
    --paper: #ffffff;
    --paper-soft: #f3f3f3;
    --charcoal: #2f3133;
    --green: #7cc142;
    --green-deep: #1e8a3c;
    --grey-text: #c9cbcd;
  }
  * { margin: 0; padding: 0; box-sizing: border-box; }
  html, body { width: 1200px; height: 913px; overflow: hidden; }
  body {
    background: var(--canvas);
    font-family: "Roboto Slab", Georgia, serif;
    position: relative;
  }
  .card {
    position: absolute;
    width: 560px;
    height: 320px;
    background: var(--paper);
    box-shadow: 0 10px 24px rgba(0,0,0,.18);
    overflow: hidden;
  }
  .card--front { left: 70px; top: 110px; }
  .card--back { left: 570px; top: 480px; background: var(--paper-soft); }

  .brand {
    position: absolute;
    display: flex;
    align-items: center;
    gap: 12px;
    color: var(--green-deep);
    font-weight: 700;
  }
  .brand__mark {
    width: 18px; height: 18px;
    flex: none;
    background: var(--green-deep);
  }
  .card--front .brand {
    left: 50%; top: 50%;
    transform: translate(-50%, -50%);
    font-size: 34px;
    white-space: nowrap;
  }
  .card--back .brand {
    left: 30px; top: 100px;
    width: 200px;
    font-size: 20px;
    line-height: 1.2;
    gap: 10px;
  }
  .card--back .brand__mark { width: 14px; height: 14px; }

  .back__tab {
    position: absolute;
    left: 0; bottom: 0;
    width: 200px; height: 62px;
    background: var(--charcoal);
    border-top-right-radius: 14px;
  }
  .back__panel {
    position: absolute;
    left: 260px; top: 0; right: 0; bottom: 0;
    background: var(--charcoal);
  }
  .back__edge {
    position: absolute;
    left: 248px; top: 0;
    width: 12px; height: 96px;
    background: var(--green);
  }
  .contact {
    position: absolute;
    left: 22px; top: 18px; right: 20px;
    color: var(--grey-text);
  }
  .contact__name { font-size: 19px; font-weight: 700; letter-spacing: .3px; }
  .contact__name span { font-weight: 400; }
  .contact__title { color: var(--green); font-size: 12px; margin-top: 2px; text-align: right; }
  .contact__rule { height: 3px; background: var(--green); margin: 5px 0 10px; width: 62%; }
  .contact__list { list-style: none; text-align: right; font-size: 12px; line-height: 20px; }
  .contact__list li { display: flex; justify-content: flex-end; align-items: center; gap: 8px; }
  .icon { width: 15px; height: 15px; flex: none; }
  .back__band {
    position: absolute;
    left: 0; right: 0; top: 222px;
    height: 42px;
    background: var(--green);
    color: var(--paper);
    font-size: 17px;
    font-weight: 700;
    letter-spacing: 1px;
    display: flex; align-items: center; justify-content: flex-end;
    padding-right: 22px;
  }
</style>
</head>
<body>
  <section class="card card--front">
    <div class="brand"><span class="brand__mark"></span>KVO Home Improvements</div>
  </section>

  <section class="card card--back">
    <div class="brand"><span class="brand__mark"></span><span>KVO Home Improvements</span></div>
    <div class="back__tab"></div>
    <div class="back__edge"></div>
    <div class="back__panel">
      <div class="contact">
        <div class="contact__name"><span>Danny</span> FERRANTE</div>
        <div class="contact__title">General Contractor</div>
        <div class="contact__rule"></div>
        <ul class="contact__list">
          <li>1-888-902-7315 Ext #1
            <svg class="icon" viewBox="0 0 16 16"><circle cx="8" cy="8" r="8" fill="#7cc142"/><path d="M5 4.5l1.6-.4 1 2-1 .8a5 5 0 0 0 2.5 2.5l.8-1 2 1-.4 1.6C8 11.5 4.5 8 5 4.5z" fill="#2f3133"/></svg></li>
          <li>215-730-4162
            <svg class="icon" viewBox="0 0 16 16"><circle cx="8" cy="8" r="8" fill="#7cc142"/><rect x="5.5" y="3.5" width="5" height="9" rx="1" fill="#2f3133"/><rect x="6.5" y="5" width="3" height="5" fill="#7cc142"/></svg></li>
          <li>1-888-902-7315
            <svg class="icon" viewBox="0 0 16 16"><circle cx="8" cy="8" r="8" fill="#7cc142"/><rect x="4" y="6.5" width="8" height="5" rx="1" fill="#2f3133"/><rect x="5.5" y="4" width="5" height="3" fill="#2f3133"/></svg></li>
          <li>info@kvoconstruction.com
            <svg class="icon" viewBox="0 0 16 16"><circle cx="8" cy="8" r="8" fill="#7cc142"/><rect x="4" y="5" width="8" height="6" rx="1" fill="#2f3133"/><path d="M4.5 5.5L8 8.5l3.5-3" fill="none" stroke="#7cc142" stroke-width="1"/></svg></li>
          <li>www.kvoconstruction.com
            <svg class="icon" viewBox="0 0 16 16"><circle cx="8" cy="8" r="8" fill="#7cc142"/><circle cx="8" cy="8" r="4" fill="none" stroke="#2f3133" stroke-width="1.2"/><path d="M4 8h8M8 4c-2 2.5-2 5.5 0 8M8 4c2 2.5 2 5.5 0 8" fill="none" stroke="#2f3133" stroke-width="1"/></svg></li>
        </ul>
      </div>
      <div class="back__band">KVO CONSTRUCTION</div>
    </div>
  </section>
</body>
</html>
```